landing page and 3 simple pages with descriptions of products

Landing page with company name. Create 3 unique pictures to link to three different pages on this this same domain.. See word document for details on the 4 pages required, the graphics/icons that need to be created. The six graphics should also be supplied for use on other marketing material.

Target Market(s)

our customer base: major laboratories across north america.

Coding

Coded - Design and coding required

Number of Pages Required

4 page

Requirements
Must have
• three images on the main page to link to the services we provide.
Nice to have
• Common theme across the title page, and the three sub pages.
• Page titles in the HTML that make sense to the items on the page.
Should not have
• scripts. sound.

```html
<!DOCTYPE html>
<html lang="en">
<head>
<meta charset="utf-8">
<title>Corvale Services Inc. – Laboratory Services</title>
<link rel="stylesheet" href="https://fonts.googleapis.com/css2?family=Lato:wght@700&family=Maven+Pro:wght@500&family=Roboto:wght@300&display=swap">
<style>
  :root {
    --brand-blue: #2162ad;
    --sky: #00bff3;
    --teal: #009a9a;
    --aqua: #33cccc;
    --orange: #ff9c00;
    --rust: #cc3300;
    --lime: #a8cf55;
    --body-text: #555555;
    --footer-bg: #000000;
    --white: #ffffff;
  }
  * { box-sizing: border-box; margin: 0; padding: 0; }
  html, body { width: 1200px; height: 711px; overflow: hidden; }
  body {
    position: relative;
    font-family: "Roboto", sans-serif;
    background: #ffffff;
  }
  .backdrop {
    position: absolute; inset: 0;
    background:
      linear-gradient(100deg, rgba(215,232,232,0.85) 0%, rgba(236,236,236,0.8) 45%, rgba(240,215,215,0.85) 100%),
      linear-gradient(180deg, #d9d4cc 0%, #c8c2ba 55%, #bdb6ae 100%);
  }
  .site-header {
    position: absolute; left: 0; top: 27px; width: 1200px; height: 49px;
    background: var(--brand-blue);
  }
  .brand-mark {
    position: absolute; left: 81px; top: 19px; width: 82px; height: 57px;
    border-radius: 41px 41px 0 0;
    background: rgba(235,235,235,0.9);
  }
  .brand-name {
    position: absolute; left: 180px; top: 36px;
    font-family: "Lato", sans-serif; font-weight: 700; font-size: 27px;
    color: var(--white); letter-spacing: 0.2px; line-height: 32px;
  }
  .phone {
    position: absolute; right: 82px; top: 36px;
    display: flex; align-items: center; gap: 8px;
    font-family: "Lato", sans-serif; font-weight: 700; font-size: 23px;
    color: var(--white); line-height: 30px;
  }
  .headline {
    position: absolute; left: 0; top: 128px; width: 1200px; text-align: center;
    font-family: "Maven Pro", sans-serif; font-weight: 500; font-size: 23.5px;
    color: var(--brand-blue);
  }
  .services {
    position: absolute; left: 81px; top: 212px;
    display: grid; grid-template-columns: repeat(6, 173.4px); grid-template-rows: repeat(2, 173.4px);
  }
  .tile {
    width: 100%; height: 100%;
    display: flex; align-items: center; justify-content: center;
  }
  .tile svg { width: 84px; height: 84px; }
  .tile--sky { background: var(--sky); }
  .tile--teal { background: var(--teal); }
  .tile--aqua { background: var(--aqua); }
  .tile--orange { background: var(--orange); }
  .tile--rust { background: var(--rust); }
  .tile--lime { background: var(--lime); }
  .service {
    padding: 23px 18px 0; text-align: center;
  }
  .service h2 {
    font-family: "Maven Pro", sans-serif; font-weight: 500; font-size: 16.5px;
    line-height: 22.5px; margin-bottom: 1px; margin-left: -12px; margin-right: -12px;
  }
  .service p {
    font-size: 13.4px; line-height: 20px; color: var(--body-text); font-weight: 300;
    letter-spacing: 0.2px;
  }
  .c-sky { color: var(--sky); }
  .c-teal { color: var(--teal); }
  .c-aqua { color: var(--aqua); }
  .c-orange { color: var(--orange); }
  .c-rust { color: var(--rust); }
  .c-lime { color: var(--lime); }
  .site-footer {
    position: absolute; left: 0; top: 657px; width: 1200px; height: 54px;
    background: var(--footer-bg);
  }
  .copyright {
    position: absolute; left: 82px; top: 18px;
    font-family: "Lato", sans-serif; font-weight: 700; font-size: 13.5px; color: var(--white);
  }
  .social {
    position: absolute; right: 80px; top: 10px; display: flex; gap: 12px; list-style: none;
  }
  .social li {
    width: 33px; height: 33px; border-radius: 50%; border: 2px solid var(--white);
  }
  .social .s1 { background: #2f5fa8; }
  .social .s2 { background: #1a76b8; }
  .social .s3 { background: #2aa3e0; }
  .social .s4 { background: #d03b26; }
</style>
</head>
<body>
  <div class="backdrop" role="img" aria-label="Faded background photo of burlap sacks and wooden boards"></div>

  <header class="site-header"></header>
  <div class="brand-mark" aria-hidden="true"></div>
  <div class="brand-name">CORVALE SERVICES INC.</div>
  <div class="phone">
    <svg width="14" height="26" viewBox="0 0 14 26" aria-hidden="true">
      <path d="M4 1 L8 1 L9 7 L6 9 Q6 13 8 17 L11 16 L13 22 L10 25 Q2 23 1 13 Q1 4 4 1 Z" fill="none" stroke="#ffffff" stroke-width="2" stroke-linejoin="round"/>
    </svg>
    <span>555-014-2290</span>
  </div>

  <h1 class="headline">Lorem ipsum dolor sit amet, consectetuer adipis</h1>

  <main class="services">
    <div class="tile tile--sky" role="img" aria-label="Microscope icon">
      <svg viewBox="0 0 80 80" aria-hidden="true">
        <g fill="#ffffff">
          <rect x="30" y="6" width="14" height="30" rx="2" transform="rotate(30 37 21)"/>
          <rect x="20" y="34" width="18" height="6" rx="1"/>
          <path d="M44 40 A18 18 0 0 1 52 70 L44 70 A12 12 0 0 0 40 46 Z"/>
          <rect x="16" y="50" width="26" height="6" rx="1"/>
          <rect x="26" y="40" width="6" height="12"/>
          <rect x="14" y="70" width="48" height="6" rx="1"/>
        </g>
      </svg>
    </div>
    <div class="service"><h2 class="c-orange">Corvale<br>Forge</h2><p>Lorem ipsum dolor sit amet, consectetuer adipiscing elit, sed diam nonummy</p></div>
    <div class="tile tile--teal" role="img" aria-label="Fish outline icon">
      <svg viewBox="0 0 100 80" aria-hidden="true" style="width:100px">
        <path d="M6 40 Q30 14 62 32 Q72 37 78 42 L94 22 Q86 42 94 62 L78 46 Q70 52 62 54 Q30 66 6 40 Z" fill="none" stroke="#ffffff" stroke-width="2.5" stroke-linejoin="round"/>
      </svg>
    </div>
    <div class="service"><h2 class="c-rust">Surplus Laboratory<br>Equipment</h2><p>Lorem ipsum dolor sit amet, consectetuer adipiscing elit, sed diam nonummy</p></div>
    <div class="tile tile--aqua" role="img" aria-label="Two rings icon">
      <svg viewBox="0 0 80 80" aria-hidden="true">
        <g fill="none" stroke="#ffffff" stroke-width="6">
          <circle cx="29" cy="44" r="17"/>
          <circle cx="51" cy="44" r="17"/>
        </g>
        <path d="M23 22 L29 16 L35 22 Z" fill="#ffffff"/>
      </svg>
    </div>
    <div class="service"><h2 class="c-lime">Corvale<br>Fabrication</h2><p>Lorem ipsum dolor sit amet, consectetuer adipiscing elit, sed diam nonummy</p></div>

    <div class="service"><h2 class="c-sky">National Laboratory<br>Services</h2><p>Lorem ipsum dolor sit amet, consectetuer adipiscing elit, sed diam nonummy</p></div>
    <div class="tile tile--orange" role="img" aria-label="Anvil and hammer icon">
      <svg viewBox="0 0 90 80" aria-hidden="true" style="width:90px">
        <g fill="#ffffff">
          <path d="M4 38 L86 34 Q80 46 64 48 L58 56 L66 62 L66 68 L24 68 L24 62 L32 56 L28 48 Q10 46 4 38 Z"/>
          <rect x="52" y="8" width="20" height="8" rx="1" transform="rotate(20 62 12)"/>
          <rect x="58" y="14" width="4" height="22" transform="rotate(20 60 25)"/>
        </g>
        <g stroke="#ffffff" stroke-width="3" stroke-linecap="round">
          <line x1="18" y1="16" x2="40" y2="76"/>
          <line x1="28" y1="14" x2="16" y2="76"/>
          <line x1="58" y1="56" x2="72" y2="76"/>
        </g>
      </svg>
    </div>
    <div class="service"><h2 class="c-teal">Corvale<br>Farms</h2><p>Lorem ipsum dolor sit amet, consectetuer adipiscing elit, sed diam nonummy</p></div>
    <div class="tile tile--rust" role="img" aria-label="Flask and test tube icon">
      <svg viewBox="0 0 80 80" aria-hidden="true">
        <g fill="none" stroke="#ffffff" stroke-width="3" stroke-linejoin="round" stroke-linecap="round">
          <path d="M24 14 L36 14 M27 14 L27 32 L12 66 Q11 70 15 70 L45 70 Q49 70 48 66 L33 32 L33 14"/>
          <path d="M54 8 L70 8 M57 8 L57 68 Q57 74 62 74 Q67 74 67 68 L67 8"/>
          <line x1="62" y1="26" x2="67" y2="26"/><line x1="62" y1="36" x2="67" y2="36"/><line x1="62" y1="46" x2="67" y2="46"/>
        </g>
        <path d="M18 54 L42 54 L46 66 L14 66 Z" fill="#ffffff"/>
        <circle cx="28" cy="46" r="3" fill="#ffffff"/>
      </svg>
    </div>
    <div class="service"><h2 class="c-aqua">Marriage<br>Commissioner</h2><p>Lorem ipsum dolor sit amet, consectetuer adipiscing elit, sed diam nonummy</p></div>
    <div class="tile tile--lime" role="img" aria-label="Rolled sheet material icon">
      <svg viewBox="0 0 90 80" aria-hidden="true" style="width:90px">
        <path d="M24 22 L52 14 Q70 14 70 32 L86 34 L66 70 L28 70 Z" fill="#ffffff"/>
        <ellipse cx="24" cy="46" rx="14" ry="24" transform="rotate(-50 24 46)" fill="#ffffff" stroke="var(--lime)" stroke-width="3"/>
        <ellipse cx="24" cy="50" rx="9" ry="15" transform="rotate(-50 24 50)" fill="none" stroke="var(--lime)" stroke-width="2"/>
      </svg>
    </div>
  </main>

  <footer class="site-footer">
    <p class="copyright">Copyright 2016 CORVALE SERVICES INC.| All Right Reserved.</p>
    <ul class="social" aria-label="Social links">
      <li class="s1"></li><li class="s2"></li><li class="s3"></li><li class="s4"></li>
    </ul>
  </footer>
</body>
</html>
```